Upscale business cards needed for family office

We would like professional business cards created for employees of our family office. Relatively simple and straightforward, but also with a unique element to set them apart. Probably stick with neutral and simple colors that mesh well with the colors in the logo. We need space for the traditional elements, including name, title, address, email/phone number.

Industry/Entity Type

Business

Contact Information for Business Card

Space for name, title, phone number, email, address

```html
<!DOCTYPE html>
<html lang="en">
<head>
<meta charset="utf-8">
<title>Harlow Family Office – Business Card</title>
<link rel="stylesheet" href="https://fonts.googleapis.com/css2?family=Crimson+Text:wght@400;600&display=swap">
<style>
  :root {
    --page-bg: #d9d4cc;
    --card-dark: #050505;
    --card-mid: #1c1c1e;
    --accent-blue: #4a82d0;
    --text-light: #ececec;
    --mark-grey: #9a9a9a;
  }
  html, body {
    margin: 0;
    width: 1200px;
    height: 1022px;
    overflow: hidden;
    background: var(--page-bg);
  }
  .business-card {
    position: absolute;
    left: 140px;
    top: 248px;
    width: 920px;
    height: 526px;
    border-radius: 4px;
    background: linear-gradient(135deg, var(--card-dark) 0%, var(--card-mid) 45%, var(--card-dark) 80%);
    box-shadow: 0 18px 40px rgba(0,0,0,0.35);
    font-family: "Crimson Text", "Times New Roman", serif;
    color: var(--text-light);
  }
  .brand-mark {
    position: absolute;
    left: 70px;
    top: 222px;
    display: flex;
    align-items: center;
    gap: 16px;
  }
  .brand-square {
    width: 34px;
    height: 34px;
    background: var(--mark-grey);
  }
  .brand-name {
    font-size: 44px;
    font-weight: 400;
    letter-spacing: 3px;
    color: var(--mark-grey);
  }
  .divider-rule {
    position: absolute;
    left: 320px;
    top: 262px;
    width: 228px;
    height: 2px;
    background: var(--accent-blue);
  }
  .contact-block {
    position: absolute;
    left: 562px;
    top: 212px;
  }
  .person-name {
    margin: 0;
    font-size: 30px;
    font-weight: 400;
    letter-spacing: 1px;
    color: var(--accent-blue);
    line-height: 38px;
  }
  .person-title {
    margin: 2px 0 20px;
    font-size: 20px;
    line-height: 24px;
  }
  .contact-line {
    display: flex;
    align-items: center;
    gap: 10px;
    font-size: 21px;
    line-height: 31px;
  }
  .contact-line .icon {
    width: 14px;
    height: 14px;
    flex: none;
  }
  .contact-line.plain { padding-left: 24px; }
  .web-domain { color: var(--accent-blue); }
</style>
</head>
<body>
  <div class="business-card">
    <div class="brand-mark">
      <div class="brand-square"></div>
      <span class="brand-name">HARLOW</span>
    </div>

    <div class="divider-rule"></div>

    <div class="contact-block">
      <h1 class="person-name">DANIEL HARLOW</h1>
      <p class="person-title">Director</p>

      <div class="contact-line plain">2816 Linden Park Ave.</div>
      <div class="contact-line plain">Pasadena CA 91105</div>

      <div class="contact-line">
        <svg class="icon" viewBox="0 0 14 14" aria-hidden="true">
          <path d="M3 1 L5.5 1 L6.5 4 L5 5.2 C5.8 7 7 8.2 8.8 9 L10 7.5 L13 8.5 L13 11 C13 12 12 13 11 13 C5.5 12.5 1.5 8.5 1 3 C1 2 2 1 3 1 Z" fill="var(--text-light)"/>
        </svg>
        <span>+1 626 555-0148</span>
      </div>
      <div class="contact-line">
        <svg class="icon" viewBox="0 0 14 14" aria-hidden="true">
          <rect x="1" y="3" width="12" height="8.5" fill="none" stroke="var(--text-light)" stroke-width="1.3"/>
          <path d="M1 3 L7 8 L13 3" fill="none" stroke="var(--text-light)" stroke-width="1.3"/>
        </svg>
        <span>info@harlowfamily.com</span>
      </div>
      <div class="contact-line">
        <svg class="icon" viewBox="0 0 14 14" aria-hidden="true">
          <circle cx="7" cy="7" r="6" fill="none" stroke="var(--text-light)" stroke-width="1.2"/>
          <ellipse cx="7" cy="7" rx="2.6" ry="6" fill="none" stroke="var(--text-light)" stroke-width="1"/>
          <line x1="1" y1="7" x2="13" y2="7" stroke="var(--text-light)" stroke-width="1"/>
        </svg>
        <span>www.<span class="web-domain">harlowfamily</span>.com</span>
      </div>
    </div>
  </div>
</body>
</html>
```